Church Website with Home Page and Member Sermon Library

I am in need of an updated design for our church website. This will include 4 pages (outlined below). We are a conservative, evangelical, Christian church. The site should be modern and clean, while still reflecting our conservative values. I already have a logo for our church, and I want the site to incorporate the logo, and match the logo/branding. Stock photos are allowed if needed, but I have uploaded some images of our church and would prefer those images to be used if possible. Any stock photos used should not include any people in the photos (scenery, nature, buildings, animals, etc. are fine).

The site will need 4 pages: Home, Support Us (Donate), Login, and Recording Library.

Page 1: Home
The home page should include the following sections:

- Navigation: Should include links to each section of the home page plus a "listen live" link which will take the user to a live-streaming site and a "support us" link which will take the user to a support/donate page.

- Announcements: Can be either a banner or some other design, but there needs to be some way for us to post announcements for visitors to see. I'm open for creative ideas in this section, but would like it not to take up a lot of room on the page.

- About Us: Should include address, service times (see attached document), and information about the church.

- Pastor Bio: A section that introduces our pastor and gives a short bio about our pastor. Would like this section to include a picture of our pastor. Somewhere in this section I would like to include this Bible reference: "And I will give you pastors according to mine heart, which shall feed you with knowledge and understanding. Jer 3:15 KJV"

- Articles of Faith (What We Believe): This should include several sub-sections each with a heading, body, and possibly 1 or more scripture references. I have attached a document to the brief that includes our articles of faith. Feel free to be creative with this section in how you lay these out and format them.

- Support Us: A small section that explains what kind of support someone can give and a link to a donation page. The link can say something like "Support Us" or "Donate Now".

- Contact form: A contact form that allows the visitor to send us a message. The contact form should ask for name, email, phone, and message.

- Footer: A footer that will be displayed on all pages of the site. This should include at a minimum a link to the home page (or a link to each individual section in the home page if you prefer), a link to "listen live", a link to "support us", a link to "contact us" (or you can put the contact form directly in the footer if you prefer), the address, and a "member login" link.

Page 2: Support Us
The donation page should include a form the visitor can fill out to make a donation. We will embed a third party form later. For this design, please just mock out the design with a basic form asking for name, phone, and email.

Page 3: Login
The recording library (detailed below) will require members to login with a shared numeric code before accessing the page. We need a design for a login screen. The screen should include navigation/footer just like all other pages, but the body of the login page will consist only of a form that asks the user to enter the access code and then a "login" button.

Page 4: Recording Library

The library page is a member-only page that will require a shared, numeric pass code to access. On this page, members will be able to access a filterable list of past sermons. The page by default should display most recent sermons, but should also include a search form that allows the member to filter the sermon list to find a particular sermon. The search form should allow the user to select a filter type (e.g. Speaker name, date, event, etc.) and type in a value to search. They should be able to add multiple filters and remove filters that have been added. Each sermon that is displayed in the result list should include basic information such as title, date, speaker, tags, etc. along with a download icon, and an embedded audio player where they can click a play button to stream it on-demand. Each sermon should also have clickable tags associated with it that can be used to find related sermons.
Updates

I have uploaded several images of our church. Feel free to incorporate these into your design if possible.

Target Market(s)

Church Members

Industry/Entity Type

Religion

Number of Pages Required

4 page

Font styles to use
Sans Serif

Colors

Designer to choose colors to be used in the design.

Requirements
Must have
• Must incorporate the logo (attached)
Nice to have
• Would like the design to incorporate pictures of our church (attached) instead of stock photos if possible.
Should not have
• Please avoid an overly cluttered design. Stock photos used should not include any people in the photos.

```html
<!DOCTYPE html>
<html lang="en">
<head>
<meta charset="utf-8">
<title>Grace Hill Chapel</title>
<link href="https://fonts.googleapis.com/css2?family=Marcellus&family=Open+Sans:ital,wght@0,400;0,600;0,700;1,400&display=swap" rel="stylesheet">
<style>
:root{
  --green:#3e6b22;
  --green-dark:#1f4a1a;
  --green-deep:#10371a;
  --cyan:#13b7d8;
  --ink:#333;
  --pale:#eff3ec;
  --line:#d6ddd2;
  --white:#fff;
  --serif:'Marcellus', serif;
  --sans:'Open Sans', Arial, sans-serif;
}
*{margin:0;padding:0;box-sizing:border-box}
html,body{width:1200px;height:4515px;overflow:hidden}
body{position:relative;font-family:var(--sans);color:var(--ink);background:var(--white)}
.abs{position:absolute}
a{text-decoration:none;color:inherit}

/* top bar + nav */
.topbar{left:0;top:0;width:1200px;height:42px;background:var(--green);color:#fff;font-size:13px;font-weight:700}
.topbar .item{position:absolute;top:12px;display:flex;align-items:center;gap:8px}
.topbar .ico{width:24px;height:24px;border-radius:50%;background:#fff;display:flex;align-items:center;justify-content:center;margin-top:-4px}
.nav{left:0;top:42px;width:1200px;height:76px;background:#fff}
.nav a{position:absolute;top:28px;font-family:var(--serif);font-size:15px;color:#222;letter-spacing:.5px;white-space:nowrap}
.nav a.active{color:var(--green)}
.nav .sep{position:absolute;top:30px;width:1px;height:16px;background:#ccc}
.brand{left:486px;top:0;width:228px;height:210px;border-radius:0 0 114px 114px;background:#fff;display:flex;align-items:center;justify-content:center;z-index:3}
.brand span{font-family:var(--serif);color:var(--green);font-size:30px;line-height:1.05;text-align:center;margin-top:30px}

/* hero */
.hero{left:0;top:118px;width:1200px;height:550px;background:linear-gradient(180deg,#8a6a44 0%,#6e5032 45%,#3f2c1c 100%)}
.hero h1{position:absolute;left:0;width:1200px;top:318px;text-align:center;font-family:var(--serif);font-weight:400;color:#fff;font-size:48px;line-height:48px;letter-spacing:1px;text-shadow:0 2px 6px rgba(0,0,0,.5)}

/* announcement strip */
.announce{left:0;top:668px;width:1200px;height:40px;background:var(--cyan);color:#fff;display:flex;align-items:center;justify-content:center;gap:14px;font-size:13px}
.announce .tag{font-family:var(--serif);letter-spacing:1px;font-size:13px;border:1px solid rgba(255,255,255,.8);padding:3px 10px}

/* pastor */
.pastor-block{left:0;top:734px;width:420px;height:430px;background:var(--green)}
.pastor-frame{left:130px;top:813px;width:429px;height:315px;border:2px solid var(--cyan)}
.pastor-photo{left:110px;top:792px;width:428px;height:314px;background:linear-gradient(160deg,#e6e2da,#b7a58a 60%,#7e5e3a)}
.eyebrow{font-size:16px;color:var(--green)}
.title{font-family:var(--serif);font-weight:400;color:var(--green);font-size:42px;letter-spacing:1px;line-height:1.2}
.divider-ico{width:14px;height:26px;display:inline-block}
.pastor-text{left:671px;top:796px;width:420px}
.pastor-text p{margin-top:14px;font-size:11px;line-height:18px;color:#444}
.pastor-text .verse{margin-top:12px;padding-left:12px;border-left:2px solid var(--cyan);font-style:italic;font-size:11px;line-height:17px;color:#555}
.pastor-text .sig{margin-top:12px;color:var(--cyan);font-size:15px}

/* service band */
.group-photo{left:0;top:1232px;width:1200px;height:501px;background:linear-gradient(180deg,#6b5d4b,#4a3a2c 50%,#7c4a3a)}
.card{background:#fff}
.card header{height:54px;background:var(--cyan);color:#fff;font-size:16px;font-weight:700;padding:17px 18px 0}
.svc-card{left:673px;top:1342px;width:317px;height:326px}
.svc-card .body{padding:18px 18px 0}
.svc-card h4{color:var(--cyan);font-size:14px;font-weight:700;margin-bottom:14px}
.row{display:flex;justify-content:space-between;font-size:13px;color:#333;height:33px}
.svc-card hr{border:0;border-top:1px solid #ddd;margin:4px 0 20px}

/* section heads */
.section-head{left:0;width:1200px;text-align:center}
.section-head .line{width:514px;height:1px;background:#cfd8cc;margin:10px auto 0}
.section-head .divider-ico{margin-top:-12px}

/* news */
.news-card{width:314px;height:388px;top:1922px}
.news-img{position:absolute;left:0;top:0;width:314px;height:238px}
.news-card .box{position:absolute;left:4px;top:186px;width:278px;height:200px;background:#fff;box-shadow:0 10px 24px rgba(0,0,0,.07)}
.news-body{position:absolute;left:4px;top:186px;width:278px;height:200px;padding:22px 26px}
.news-body .date{font-size:13px;color:#444}
.news-body h3{font-family:var(--serif);font-weight:400;color:var(--green);font-size:15px;margin:6px 0 14px;letter-spacing:.5px}
.news-body p{font-size:10.5px;line-height:16px;color:#444}

/* sermons */
.sermons{left:0;top:2398px;width:1200px;height:677px;background:var(--pale)}
.slide{position:absolute}
.arrow{position:absolute;width:32px;height:32px;border-radius:50%;background:#fff;display:flex;align-items:center;justify-content:center}
.play{position:absolute;left:584px;top:2742px;width:42px;height:42px;border-radius:50%;background:var(--green);border:3px solid #fff;display:flex;align-items:center;justify-content:center}
.btn-outline{position:absolute;border:2px solid #9aa892;background:#e4eadf;font-family:var(--serif);font-size:12px;color:var(--green);letter-spacing:1px;display:flex;align-items:center;justify-content:center;gap:6px}

/* articles of faith */
.faith{left:0;top:3075px;width:1200px;height:534px;background:radial-gradient(ellipse at center,#1e5a28 0%,var(--green-deep) 78%);color:#fff}
.faith .head{position:absolute;left:0;top:52px;width:1200px;text-align:center}
.faith .eyebrow{color:#b9d6a3}
.faith .title{color:#fff;font-size:38px}
.faith .rule{width:514px;height:1px;background:rgba(255,255,255,.35);margin:10px auto 0}
.article{position:absolute;top:200px;width:230px;height:290px;border:1px solid rgba(255,255,255,.22);background:rgba(255,255,255,.05);padding:24px 20px}
.article h3{font-family:var(--serif);font-weight:400;font-size:19px;letter-spacing:.5px;margin-bottom:6px}
.article .bar{width:30px;height:2px;background:var(--cyan);margin-bottom:14px}
.article p{font-size:12px;line-height:19px;color:#e5eee0}
.article .ref{position:absolute;left:20px;bottom:22px;font-size:12px;font-weight:600;color:var(--cyan)}

/* contact */
.contact-info{left:210px;top:3700px;width:300px}
.contact-info h4{color:var(--green);font-size:13px;font-weight:700;margin-bottom:10px}
.contact-info .row{font-size:12px;height:29px;width:170px}
.contact-info h3{font-family:var(--serif);font-weight:400;color:var(--green);font-size:20px;margin:36px 0 14px;letter-spacing:.5px}
.map{left:590px;top:3609px;width:610px;height:517px;background:linear-gradient(135deg,#eef0ec,#e3e6df)}
.form-card{left:660px;top:3654px;width:340px;height:426px;box-shadow:0 10px 28px rgba(0,0,0,.12)}
.form-card form{padding:20px 20px 0}
.field{display:block;width:100%;height:38px;border:1px solid var(--line);margin-bottom:12px;padding:0 12px;font-family:var(--sans);font-size:13px;color:#888;display:flex;align-items:center}
.field.msg{height:96px;align-items:flex-start;padding-top:10px}
.send{width:100%;height:42px;background:var(--green);color:#fff;border:0;font-family:var(--serif);font-size:14px;letter-spacing:1px;margin-top:4px}

/* footer */
.footer{left:0;top:4126px;width:1200px;height:389px;background:var(--cyan);color:#fff}
.footer h5{font-family:var(--serif);font-weight:400;font-size:14px;letter-spacing:1px;margin-bottom:12px}
.footer ul{list-style:none;font-size:11px;line-height:22px}
.footer .col{position:absolute;top:72px}
.footer .vline{position:absolute;top:100px;width:1px;height:150px;background:rgba(255,255,255,.35)}
.social{width:30px;height:30px;border-radius:50%;background:#fff;display:inline-block;margin-right:6px}
.copy{position:absolute;left:0;width:1200px;top:358px;text-align:center;font-size:11px}
</style>
</head>
<body>

<div class="abs topbar">
  <div class="item" style="left:210px"><span class="ico"><svg width="12" height="14" viewBox="0 0 12 14"><path d="M6 0a5 5 0 0 0-5 5c0 4 5 9 5 9s5-5 5-9a5 5 0 0 0-5-5zm0 7a2 2 0 1 1 0-4 2 2 0 0 1 0 4z" fill="#13b7d8"/></svg></span>214 Meadow Ln. Ashford, NC 27012</div>
  <div class="item" style="left:852px"><span class="ico"><svg width="13" height="13" viewBox="0 0 24 24"><path d="M6.6 10.8a15 15 0 0 0 6.6 6.6l2.2-2.2a1 1 0 0 1 1-.25 11 11 0 0 0 3.6.6 1 1 0 0 1 1 1V20a1 1 0 0 1-1 1A17 17 0 0 1 3 4a1 1 0 0 1 1-1h3.5a1 1 0 0 1 1 1 11 11 0 0 0 .6 3.6 1 1 0 0 1-.25 1z" fill="#13b7d8"/></svg></span>+1 555-014-2270</div>
</div>

<nav class="abs nav">
  <a href="#" class="active" style="left:190px">HOME</a>
  <span class="sep" style="left:272px"></span>
  <a href="#" style="left:300px">SERVICE TIMES</a>
  <a href="#" style="left:740px">LIBRARY</a>
  <span class="sep" style="left:823px"></span>
  <a href="#" style="left:845px">LISTEN LIVE</a>
  <span class="sep" style="left:957px"></span>
  <a href="#" style="left:979px">DONATION</a>
</nav>
<div class="abs brand"><span>GRACE HILL<br>CHAPEL</span></div>

<section class="abs hero" role="img" aria-label="Church sanctuary with wooden cross, pulpit and pews">
  <h1>WE BELIEVE DIVINE GRACE HILL<br>CHAPEL</h1>
</section>

<div class="abs announce">
  <span class="tag">ANNOUNCEMENT</span>
  <span>Fellowship dinner follows the Sunday evening service this week. All are welcome.</span>
</div>

<!-- pastor -->
<div class="abs pastor-block"></div>
<div class="abs pastor-frame"></div>
<div class="abs pastor-photo" role="img" aria-label="Pastor speaking at the pulpit decorated with flowers"></div>
<div class="abs pastor-text">
  <div class="eyebrow">Pastor Bio</div>
  <h2 class="title">MEET OUR PASTOR</h2>
  <svg class="divider-ico" viewBox="0 0 14 26"><path d="M2 25V8a5 5 0 0 1 10 0v17z" fill="none" stroke="#13b7d8" stroke-width="1.5"/></svg>
  <p>Lorem Ipsum Dolor Sit Amet, Consectetur Adipiscing Elit. Curabitur Eu Urna Fermentum, Dignissim Elit Ac, Pharetra Mauris. Duis Ante Neque, Dapibus Eu Metus Quis, Tempus Fermentum Nibh. Orci Varius Natoque Penatibus Et Magnis Dis Parturient Montes, Nascetur Ridiculus Mus. Nunc Arcu Mauris, Sollicitudin Nec Nisi Eu, Ultrices Posuere Mi. Duis Lectus Arcu, Iaculis Non Venenatis Vitae, Ultricies Quis Lectus. Duis A Sollicitudin Urna, A Vulputate Dolor. Cras Ut Leo Justo.</p>
  <div class="verse">“And I will give you pastors according to mine heart, which shall feed you with knowledge and understanding.” Jer 3:15 KJV</div>
  <div class="sig">-PASTOR DALE MORGAN</div>
</div>

<!-- service times -->
<div class="abs group-photo" role="img" aria-label="Congregation group gathered in the fellowship hall"></div>
<div class="abs card svc-card">
  <header>Service Times</header>
  <div class="body">
    <h4>Sunday Services:</h4>
    <div class="row"><span>Sunday School -</span><span>9:45 AM</span></div>
    <div class="row"><span>Morning Worship -</span><span>10:45 AM</span></div>
    <div class="row"><span>Evening Service -</span><span>6:00 PM</span></div>
    <hr>
    <h4>Midweek Service:</h4>
    <div class="row"><span>Wednesday -</span><span>7:00 PM</span></div>
  </div>
</div>

<!-- news -->
<div class="abs section-head" style="top:1796px">
  <div class="eyebrow" style="color:#6f8f55">Prayer &amp; Praise Reports</div>
  <h2 class="title" style="font-size:36px">OUR LATEST NEWS</h2>
  <div class="line"></div>
  <svg class="divider-ico" viewBox="0 0 14 26" style="background:#fff"><path d="M2 25V8a5 5 0 0 1 10 0v17z" fill="none" stroke="#13b7d8" stroke-width="1.5"/></svg>
</div>

<article class="abs news-card" style="left:110px">
  <div class="news-img" role="img" aria-label="Family standing before the church cross" style="background:linear-gradient(160deg,#ece6da,#b49a78 60%,#7e5f3c)"></div>
  <div class="box"></div>
  <div class="news-body"><div class="date">3/8/2020</div><h3>IDOL OF MONEY</h3><p>Lorem Ipsum Dolor Sit Amet, Consectetur Adipiscing Elit. Curabitur Eu Urna Fermentum, Dignissim Elit Ac, Pharetra Mauris. Duis Ante Neque, Dapibus Eu Metus Quis, Tempus Fermentum Nibh. Orci Varius Natoque Penatibus Et Magnis Dis Parturient</p></div>
</article>
<article class="abs news-card" style="left:443px">
  <div class="news-img" role="img" aria-label="Church member portrait" style="background:linear-gradient(160deg,#efeae2,#c4b8aa 60%,#6b6a78)"></div>
  <div class="box"></div>
  <div class="news-body"><div class="date">3/8/2020</div><h3>IDOL OF MONEY</h3><p>Lorem Ipsum Dolor Sit Amet, Consectetur Adipiscing Elit. Curabitur Eu Urna Fermentum, Dignissim Elit Ac, Pharetra Mauris. Duis Ante Neque, Dapibus Eu Metus Quis, Tempus Fermentum Nibh. Orci Varius Natoque Penatibus Et Magnis Dis Parturient</p></div>
  <div class="abs" style="left:4px;top:384px;width:278px;height:4px;background:var(--cyan)"></div>
</article>
<svg class="abs" style="left:642px;top:2278px" width="116" height="56" viewBox="0 0 116 56"><g fill="#13b7d8">
  <circle cx="2" cy="54" r="1.6"/><circle cx="10" cy="54" r="1.6"/><circle cx="18" cy="54" r="1.6"/><circle cx="26" cy="54" r="1.6"/><circle cx="34" cy="54" r="1.6"/><circle cx="42" cy="54" r="1.6"/><circle cx="50" cy="54" r="1.6"/><circle cx="58" cy="54" r="1.6"/><circle cx="66" cy="54" r="1.6"/><circle cx="74" cy="54" r="1.6"/><circle cx="82" cy="54" r="1.6"/><circle cx="90" cy="54" r="1.6"/>
  <circle cx="98" cy="2" r="1.6"/><circle cx="106" cy="2" r="1.6"/><circle cx="114" cy="2" r="1.6"/><circle cx="98" cy="12" r="1.6"/><circle cx="106" cy="12" r="1.6"/><circle cx="114" cy="12" r="1.6"/><circle cx="98" cy="22" r="1.6"/><circle cx="106" cy="22" r="1.6"/><circle cx="114" cy="22" r="1.6"/><circle cx="98" cy="32" r="1.6"/><circle cx="106" cy="32" r="1.6"/><circle cx="114" cy="32" r="1.6"/><circle cx="98" cy="42" r="1.6"/><circle cx="106" cy="42" r="1.6"/><circle cx="114" cy="42" r="1.6"/><circle cx="98" cy="54" r="1.6"/><circle cx="106" cy="54" r="1.6"/></g></svg>
<article class="abs news-card" style="left:776px">
  <div class="news-img" role="img" aria-label="Young men of the congregation" style="background:linear-gradient(160deg,#d8d2c8,#a88f70 55%,#5b4b3e)"></div>
  <div class="box"></div>
  <div class="news-body"><div class="date">3/8/2020</div><h3>IDOL OF MONEY</h3><p>Lorem Ipsum Dolor Sit Amet, Consectetur Adipiscing Elit. Curabitur Eu Urna Fermentum, Dignissim Elit Ac, Pharetra Mauris. Duis Ante Neque, Dapibus Eu Metus Quis, Tempus Fermentum Nibh. Orci Varius Natoque Penatibus Et Magnis Dis Parturient</p></div>
</article>

<!-- sermons -->
<section class="abs sermons"></section>
<div class="abs section-head" style="top:2460px">
  <div class="eyebrow" style="color:#6f8f55">Member Sermon Library</div>
  <h2 class="title" style="font-size:36px">LIVE-STREAMING SERVICES</h2>
  <div class="line"></div>
  <svg class="divider-ico" viewBox="0 0 14 26" style="background:var(--pale)"><path d="M2 25V8a5 5 0 0 1 10 0v17z" fill="none" stroke="#13b7d8" stroke-width="1.5"/></svg>
</div>
<div class="slide" role="img" aria-label="Worship service in the sanctuary" style="left:110px;top:2621px;width:212px;height:282px;background:linear-gradient(160deg,#d9d9d9,#8e8e8e 60%,#3c3c3c)"></div>
<div class="slide" role="img" aria-label="Preacher at the pulpit during a service" style="left:322px;top:2591px;width:556px;height:344px;background:linear-gradient(160deg,#efe3c6,#c7a56e 55%,#6b4a28)"></div>
<div class="slide" role="img" aria-label="Men reading scripture together" style="left:878px;top:2621px;width:212px;height:282px;background:linear-gradient(160deg,#b69e7d,#6e5740 55%,#2f2a28)"></div>
<div class="arrow" style="left:305px;top:2747px"><svg width="14" height="12" viewBox="0 0 14 12"><path d="M7 1 2 6l5 5M12 1 7 6l5 5" fill="none" stroke="#13b7d8" stroke-width="1.6"/></svg></div>
<div class="arrow" style="left:860px;top:2747px"><svg width="14" height="12" viewBox="0 0 14 12"><path d="M2 1l5 5-5 5M7 1l5 5-5 5" fill="none" stroke="#13b7d8" stroke-width="1.6"/></svg></div>
<div class="play"><svg width="14" height="16" viewBox="0 0 14 16"><path d="M2 1l11 7-11 7z" fill="#fff"/></svg></div>
<a class="btn-outline" href="#" style="left:504px;top:2968px;width:185px;height:38px">LISTEN LIVE</a>

<!-- articles of faith -->
<section class="abs faith">
  <div class="head">
    <div class="eyebrow">What We Believe</div>
    <h2 class="title">ARTICLES OF FAITH</h2>
    <div class="rule"></div>
  </div>
  <div class="article" style="left:110px">
    <h3>The Scriptures</h3><div class="bar"></div>
    <p>We believe the Holy Bible is the inspired, infallible Word of God, the final authority for faith and practice in every part of life.</p>
    <div class="ref">2 Tim 3:16</div>
  </div>
  <div class="article" style="left:360px">
    <h3>The Godhead</h3><div class="bar"></div>
    <p>We believe in one God, eternally existing in three persons: the Father, the Son and the Holy Spirit, equal in power and glory.</p>
    <div class="ref">Matt 28:19</div>
  </div>
  <div class="article" style="left:610px">
    <h3>Salvation</h3><div class="bar"></div>
    <p>We believe salvation is by grace through faith in the shed blood of Jesus Christ, who died for our sins and rose again.</p>
    <div class="ref">Eph 2:8-9</div>
  </div>
  <div class="article" style="left:860px">
    <h3>Holiness</h3><div class="bar"></div>
    <p>We believe God calls His people to a holy life, set apart from sin and wholly given to Him in heart, word and conduct.</p>
    <div class="ref">1 Pet 1:15-16</div>
  </div>
</section>

<!-- contact -->
<div class="abs contact-info">
  <h4>Service Times</h4>
  <div class="row"><span>Sunday School -</span><span>9:45 AM</span></div>
  <div class="row"><span>Morning Worship -</span><span>10:45 AM</span></div>
  <div class="row"><span>Evening Service -</span><span>6:00 PM</span></div>
  <h4 style="margin-top:8px">Midweek Service:</h4>
  <div class="row"><span>Wednesday -</span><span>7:00 PM</span></div>
  <h3>GRACE HILL CHAPEL</h3>
  <div style="display:flex;gap:6px;font-size:12px;line-height:15px"><svg width="12" height="14" viewBox="0 0 12 14"><path d="M6 0a5 5 0 0 0-5 5c0 4 5 9 5 9s5-5 5-9a5 5 0 0 0-5-5zm0 7a2 2 0 1 1 0-4 2 2 0 0 1 0 4z" fill="#13b7d8"/></svg><span>214 Meadow Ln.<br>Ashford, NC 27012</span></div>
  <a class="btn-outline" href="#" style="position:relative;margin-top:28px;width:160px;height:40px">♡ DONATION</a>
</div>
<div class="abs map" role="img" aria-label="Street map showing the church location"></div>
<div class="abs card form-card">
  <header>Contact Us</header>
  <form>
    <div class="field">Name</div>
    <div class="field">Email</div>
    <div class="field">Phone</div>
    <div class="field msg">Message</div>
    <button class="send" type="button">SEND MESSAGE</button>
  </form>
</div>

<!-- footer -->
<footer class="abs footer">
  <div class="abs" style="left:200px;top:96px;width:180px;text-align:center;font-family:var(--serif);font-size:28px;line-height:32px">GRACE HILL<br>CHAPEL</div>
  <div class="abs" style="left:232px;top:186px"><span class="social" aria-label="Social link"></span><span class="social" style="background:var(--green)" aria-label="Social link"></span><span class="social" aria-label="Social link"></span></div>
  <div class="col" style="left:430px"><h5>QUICK LINKS</h5><ul><li>Home</li><li>About Us</li><li>Service Times</li><li>Listen Live</li><li>Support Us</li><li>Contact Us</li><li>Member Login</li></ul></div>
  <span class="vline" style="left:568px"></span>
  <div class="col" style="left:608px"><h5>SERVICE TIMES</h5><ul><li>Sunday School - 9:45 AM</li><li>Morning Worship - 10:45 AM</li><li>Evening Service - 6:00 PM</li></ul><h5 style="margin:6px 0 6px">MIDWEEK SERVICE:</h5><ul><li>Wednesday - 7:00 PM</li></ul></div>
  <span class="vline" style="left:800px"></span>
  <div class="col" style="left:845px"><h5>LOCATION</h5><ul style="line-height:16px;font-weight:700"><li>214 Meadow Ln.</li><li>Ashford, NC 27012</li></ul><h5 style="margin:12px 0 8px">CALL US</h5><ul style="font-weight:700"><li>☏ +1 555-014-2270</li></ul><h5 style="margin:10px 0 8px">CONTACT US</h5><ul><li>✉ office@gracehillchapel.org</li></ul></div>
  <div class="copy">© 2023 Grace Hill Chapel All Right Reserved.</div>
</footer>

</body>
</html>
```